Business Cards - New Logo Rebranding

Hello We know have a red and blue logo and are looking to create new cards. We are looking for the best creativity of the new logo merged with some of the existing artwork provided.

Target Market(s)

Realtors

Industry/Entity Type

Real Estate

Contact Information for Business Card

New logo with rebranded colors

Requirements
Must have
• Creative use of the new logo

```html
<!DOCTYPE html>
<html lang="en">
<head>
<meta charset="utf-8">
<title>Summit Crest Business Cards</title>
<link rel="stylesheet" href="https://fonts.googleapis.com/css2?family=Lato:wght@400;700;900&family=Oswald:wght@500&display=swap">
<style>
  :root {
    --stage: #2b2d31;
    --card: #ffffff;
    --brand-blue: #0b6cc4;
    --brand-red: #e0313f;
    --ink: #5d5f63;
    --rule: #e4e5e8;
  }
  * { box-sizing: border-box; margin: 0; padding: 0; }
  html, body { width: 1200px; height: 952px; overflow: hidden; }
  body {
    background: var(--stage);
    font-family: "Lato", sans-serif;
    position: relative;
  }
  .card {
    position: absolute;
    left: 240px;
    width: 720px;
    height: 411px;
    background: var(--card);
    overflow: hidden;
    box-shadow: 0 10px 30px rgba(0,0,0,.35);
  }
  .card--front { top: 50px; }
  .card--back { top: 491px; }

  .accent-bar { position: absolute; background: var(--brand-blue); }
  .accent-bar--left { left: 0; top: 70px; width: 22px; height: 190px; }
  .accent-bar--right { right: 0; top: 170px; width: 32px; height: 190px; }

  .brand {
    position: absolute;
    display: flex;
    align-items: center;
    gap: 12px;
  }
  .brand__dot {
    width: 48px; height: 48px;
    border-radius: 50%;
    background: var(--brand-red);
    flex: none;
  }
  .brand__name {
    font-weight: 900;
    color: var(--brand-blue);
    text-transform: uppercase;
    letter-spacing: 1px;
    line-height: 1;
    white-space: nowrap;
  }
  .brand__sub {
    font-size: 8px;
    font-weight: 700;
    color: var(--brand-blue);
    letter-spacing: 1px;
    text-transform: uppercase;
    margin-top: 5px;
    white-space: nowrap;
  }
  .card--front .brand { left: 60px; top: 100px; }
  .card--front .brand__name { font-size: 22px; }

  .divider {
    position: absolute;
    left: 340px; top: 60px;
    width: 1px; height: 200px;
    background: var(--rule);
  }

  .contact { position: absolute; left: 372px; top: 95px; color: var(--ink); }
  .contact__name { font-size: 28px; font-weight: 700; letter-spacing: 1px; text-transform: uppercase; white-space: nowrap; }
  .contact__first { color: var(--brand-red); font-weight: 400; }
  .contact__last { color: var(--brand-blue); font-weight: 900; }
  .contact__role { font-size: 18px; margin-top: 2px; }
  .contact__list { list-style: none; margin-top: 16px; }
  .contact__item {
    display: flex; align-items: center; gap: 10px;
    font-size: 16px; line-height: 27px; white-space: nowrap;
  }
  .contact__icon { width: 14px; height: 14px; flex: none; }

  .address {
    position: absolute; left: 60px; bottom: 40px;
    font-size: 15px; color: var(--ink);
  }

  .card--back .brand-block {
    position: absolute; left: 0; right: 0; top: 130px;
    display: flex; flex-direction: column; align-items: center;
  }
  .card--back .brand__name { font-size: 50px; }
  .card--back .brand__sub { font-size: 11px; letter-spacing: 3px; margin-top: 8px; }
  .services {
    margin-top: 14px;
    font-family: "Oswald", sans-serif;
    font-weight: 500;
    font-size: 18px;
    color: var(--brand-blue);
    text-transform: uppercase;
    letter-spacing: .5px;
  }
  .services__sep { color: var(--brand-red); padding: 0 6px; }
</style>
</head>
<body>

<section class="card card--front" aria-label="Business card front">
  <div class="accent-bar accent-bar--left"></div>
  <div class="accent-bar accent-bar--right"></div>

  <div class="brand">
    <div class="brand__dot"></div>
    <div>
      <div class="brand__name">Summit Crest</div>
      <div class="brand__sub">Inspection Professionals</div>
    </div>
  </div>

  <div class="divider"></div>

  <div class="contact">
    <div class="contact__name"><span class="contact__first">Daniel R.</span> <span class="contact__last">Hartley</span></div>
    <div class="contact__role">Managing Director</div>
    <ul class="contact__list">
      <li class="contact__item">
        <svg class="contact__icon" viewBox="0 0 24 24"><path fill="#e0313f" d="M6.6 10.8a15.1 15.1 0 0 0 6.6 6.6l2.2-2.2a1 1 0 0 1 1-.25 11.4 11.4 0 0 0 3.6.57 1 1 0 0 1 1 1V20a1 1 0 0 1-1 1A17 17 0 0 1 3 4a1 1 0 0 1 1-1h3.5a1 1 0 0 1 1 1c0 1.25.2 2.45.57 3.57a1 1 0 0 1-.25 1z"/></svg>
        +00 555 210 48
      </li>
      <li class="contact__item">
        <svg class="contact__icon" viewBox="0 0 24 24"><path fill="#e0313f" d="M2 5h20v14H2z"/><path fill="none" stroke="#fff" stroke-width="2" d="M2 5l10 8 10-8"/></svg>
        hello@summitcrest.com
      </li>
      <li class="contact__item">
        <svg class="contact__icon" viewBox="0 0 24 24"><circle cx="12" cy="12" r="10" fill="#e0313f"/><path fill="none" stroke="#fff" stroke-width="1.6" d="M2 12h20M12 2c3 3 3 17 0 20M12 2c-3 3-3 17 0 20"/></svg>
        www.summitcrestinspect.com
      </li>
    </ul>
  </div>

  <p class="address">2170 Harbor View Avenue Springfield, IL 62704</p>
</section>

<section class="card card--back" aria-label="Business card back">
  <div class="brand-block">
    <div class="brand__name">Summit Crest</div>
    <div class="brand__sub">Inspection Professionals</div>
    <div class="services">
      Home<span class="services__sep">•</span>Sewer<span class="services__sep">•</span>Mold<span class="services__sep">•</span>Commercial<span class="services__sep">•</span>Termite<span class="services__sep">•</span>Roof
    </div>
  </div>
</section>

</body>
</html>
```